I need email signatures for my admin staff members
info:
Darina Qubrosi
Support Coordinator
Unit 4, 517 Wattlebrook Lane, Kemberly NSW 2893
Tel: 02 84427193 Mob: 0427596314
email: darina.qu@mivrotelhaven.com
www.mivrotelhaven.com

Target Market(s)

community services industry

Industry/Entity Type

Community Service

Requirements
Must have
• Specialist Provider of Multicultural Support Services
Nice to have
• "I acknowledge the traditional owners of the land on which we live, work and dream"
plus their flags as attached

```html
<!DOCTYPE html>
<html lang="en">
<head>
<meta charset="utf-8">
<title>Email Signatures – Darina Qubrosi</title>
<link rel="stylesheet" href="https://fonts.googleapis.com/css2?family=Arimo:wght@400;700&family=Montserrat:wght@600&display=swap">
<style>
  :root {
    --orange: #f7941d;
    --charcoal: #333333;
    --blush: #fdeee0;
    --white: #ffffff;
    --ink: #231f20;
  }
  * { margin: 0; padding: 0; box-sizing: border-box; }
  html, body { width: 1200px; height: 1200px; overflow: hidden; background: var(--white); }
  .canvas { position: relative; width: 1200px; height: 1200px; font-family: "Arimo", Arial, sans-serif; }
  .shapes { position: absolute; inset: 0; }
  .abs { position: absolute; white-space: nowrap; }
  .staff-name { color: var(--white); font-weight: 700; font-size: 26px; line-height: 1; letter-spacing: -0.2px; }
  .staff-role { color: var(--ink); font-weight: 700; font-size: 13px; line-height: 1; }
  .brand-name { font-family: "Montserrat", Arial, sans-serif; font-weight: 600; color: var(--orange); line-height: 1; letter-spacing: 1px; }
  .contact { color: var(--white); font-size: 16.5px; line-height: 20px; text-align: right; }
  .contact-row { display: flex; justify-content: flex-end; align-items: flex-start; gap: 14px; }
  .contact-row + .contact-row { margin-top: 7px; }
  .contact-row svg { width: 20px; height: 20px; flex: none; }
  .web { color: var(--orange); font-weight: 700; font-size: 15px; line-height: 1; letter-spacing: 0.3px; }
</style>
</head>
<body>
<div class="canvas">
  <svg class="shapes" width="1200" height="1200" viewBox="0 0 1200 1200" aria-hidden="true">
    <defs>
      <symbol id="icon-pin" viewBox="0 0 20 20"><path d="M10 1.5a6.5 6.5 0 0 0-6.5 6.5c0 4.6 6.5 10.5 6.5 10.5s6.5-5.9 6.5-10.5A6.5 6.5 0 0 0 10 1.5z" fill="none" stroke="#f7941d" stroke-width="2"/></symbol>
      <symbol id="icon-phone" viewBox="0 0 20 20"><path d="M15.5 2.5c-5 1-10 6.5-11 13.5l2.8 1.5 1.6-3.4-1.6-1.3c1-2.6 2.8-4.6 5.2-6l1.4 1.5 3.2-1.8z" fill="#f7941d"/></symbol>
      <symbol id="icon-mail" viewBox="0 0 20 20"><rect x="1.5" y="4" width="17" height="12" fill="none" stroke="#f7941d" stroke-width="1.6"/><path d="M1.5 4 10 11l8.5-7M1.5 16l6-5.5M18.5 16l-6-5.5" fill="none" stroke="#f7941d" stroke-width="1.6"/></symbol>
    </defs>
    <!-- signature one -->
    <polygon points="158,174 472,174 438,227 158,227" fill="var(--orange)"/>
    <circle cx="546" cy="226" r="46" fill="var(--orange)"/>
    <path d="M658,174 H1042 V299 H694 C706,258 700,208 658,174 Z" fill="var(--charcoal)"/>
    <!-- signature two -->
    <rect x="179" y="472" width="842" height="255" fill="var(--blush)"/>
    <circle cx="402" cy="565" r="66" fill="var(--orange)"/>
    <polygon points="542,486 879,486 838,538 542,538" fill="var(--orange)"/>
    <path d="M546,571 H979 V696 H624 C620,640 595,595 546,571 Z" fill="var(--charcoal)"/>
    <!-- signature three -->
    <circle cx="202" cy="933" r="84" fill="var(--orange)"/>
    <polygon points="311,858 608,858 650,910 311,910" fill="var(--orange)"/>
    <polygon points="626,870 1082,870 1082,995 728,995" fill="var(--charcoal)"/>
  </svg>

  <!-- signature one -->
  <section class="signature signature--compact">
    <div class="abs staff-name" style="left:179px; top:188px;">Darina Qubrosi</div>
    <div class="abs staff-role" style="left:182px; top:236px;">SUPPORT COORDINATOR</div>
    <div class="abs brand-name" style="left:546px; top:280px; transform:translateX(-50%); font-size:28px;">MIVROTEL HAVEN</div>
    <div class="abs contact" style="right:185px; top:190px;">
      <div class="contact-row"><span>Unit 4, 517 Wattlebrook Lane,<br>Kemberly NSW 2893</span><svg><use href="#icon-pin"/></svg></div>
      <div class="contact-row"><span>02 84427193 - 0427596314</span><svg><use href="#icon-phone"/></svg></div>
      <div class="contact-row"><span>darina.qu@mivrotelhaven.com</span><svg><use href="#icon-mail"/></svg></div>
    </div>
    <div class="abs web" style="right:158px; top:304px;">www.mivrotelhaven.com</div>
  </section>

  <!-- signature two -->
  <section class="signature signature--panel">
    <div class="abs brand-name" style="left:401px; top:645px; transform:translateX(-50%); font-size:36px;">MIVROTEL HAVEN</div>
    <div class="abs staff-name" style="left:563px; top:500px;">Darina Qubrosi</div>
    <div class="abs staff-role" style="left:566px; top:548px;">SUPPORT COORDINATOR</div>
    <div class="abs contact" style="right:262px; top:588px;">
      <div class="contact-row"><span>Unit 4, 517 Wattlebrook Lane,<br>Kemberly NSW 2893</span><svg><use href="#icon-pin"/></svg></div>
      <div class="contact-row"><span>02 84427193 - 0427596314</span><svg><use href="#icon-phone"/></svg></div>
      <div class="contact-row"><span>darina.qu@mivrotelhaven.com</span><svg><use href="#icon-mail"/></svg></div>
    </div>
    <div class="abs web" style="right:222px; top:701px;">www.mivrotelhaven.com</div>
  </section>

  <!-- signature three -->
  <section class="signature signature--wide">
    <div class="abs staff-name" style="left:333px; top:873px;">Darina Qubrosi</div>
    <div class="abs staff-role" style="right:550px; top:920px;">SUPPORT COORDINATOR</div>
    <div class="abs brand-name" style="left:314px; top:944px; font-size:35px;">MIVROTEL HAVEN</div>
    <div class="abs contact" style="right:144px; top:886px;">
      <div class="contact-row"><span>Unit 4, 517 Wattlebrook Lane,<br>Kemberly NSW 2893</span><svg><use href="#icon-pin"/></svg></div>
      <div class="contact-row"><span>02 84427193 - 0427596314</span><svg><use href="#icon-phone"/></svg></div>
      <div class="contact-row"><span>darina.qu@mivrotelhaven.com</span><svg><use href="#icon-mail"/></svg></div>
    </div>
    <div class="abs web" style="right:122px; top:1001px;">www.mivrotelhaven.com</div>
  </section>
</div>
</body>
</html>
```